Yoga Training Cerificate

Design a certificate of graduation from a Vinyasa Yoga Teacher Training Program.

The attached document is an example of the certificate I received as a graduate from a teacher training program. You can use it as a template.

Stylistically, what you design can be: visually enticing, professional, clean, and modern.

Please develop the "Lumen Stretch" logo and embed it within the certificate.

Please add a circular watermark behind the body of the certificate similar to the one found in the attachment; leave out the words Asana Guildhall because I am not associated with that organization.

The name of my school is "Lumen Stretch." And it was established in 2017, which you can include.

The certificate affirms that "' 'such-and-such' has successfully completed the Lumen Stretch modern vinyasa yoga training, completing two hundred hours of instruction in practice and theory. Within the power of our institution as a certifying agent we declare Such-and-such, now, a teacher competent to share the gift of yoga with the masses in a safe and effective."

My name -Dennis Whitcombe- should be at bottom with a faux-signature; position title: Lumen Stretch founder.

If you decide to include text on the fringe, like the example, it might include bars of text describing the maxims of the Lumen Stretch school reading:

This is Lumen Stretch
Breath is primary
Evolve the physical culture
Bring your unique expression to the practice
Take Breaks
Freestyle
Close your eyes
Feel deeper into your body
This is active meditation
This is moving meditation
This is modern meditation

And find a way to integrate Emojis like: Fire, Water, Prayer Hands, etc. as you see fit.

Generally, make the certificate look: official, clear and clean. You can base it from the example given. And try and create a graphic design that is more visually capturing then the example.

```html
<!DOCTYPE html>
<html lang="en">
<head>
<meta charset="utf-8">
<title>Lumen Stretch – Certificate of Completion</title>
<link rel="stylesheet" href="https://fonts.googleapis.com/css2?family=Pinyon+Script&family=Open+Sans:wght@400;600&family=Lora:ital,wght@0,400;1,600&display=swap">
<style>
  :root {
    --backdrop: #e9e6e0;
    --paper: #efede8;
    --paper-edge: #d9d5cd;
    --ink: #2f2724;
    --ink-soft: #6d6561;
    --rule: #4a403c;
    --watermark: #d8d4cd;
    --seal: #a3161c;
    --seal-dark: #6f0c10;
  }
  * { box-sizing: border-box; margin: 0; padding: 0; }
  html, body { width: 1200px; height: 798px; overflow: hidden; }
  body {
    background: var(--backdrop);
    font-family: "Open Sans", Arial, sans-serif;
    color: var(--ink);
    position: relative;
  }
  .certificate {
    position: absolute;
    left: 60px; top: 49px;
    width: 1080px; height: 700px;
    background: var(--paper);
    border: 1px solid var(--paper-edge);
    box-shadow: 0 6px 22px rgba(60,45,35,.18);
    overflow: hidden;
  }
  .watermark {
    position: absolute;
    left: 545px; top: 110px;
    width: 380px; height: 380px;
    border-radius: 50%;
    border: 24px solid var(--watermark);
    opacity: .55;
  }
  .maxims {
    position: absolute;
    left: 70px; top: 200px;
    list-style: none;
    font-size: 14px;
    line-height: 1.35;
    color: var(--ink-soft);
  }
  .maxims li { margin-bottom: 9px; }
  .column-rule {
    position: absolute;
    left: 390px; top: 170px;
    width: 1.5px; height: 380px;
    background: var(--rule);
  }
  .brand {
    position: absolute;
    left: 100px; top: 590px;
    display: flex; align-items: center; gap: 10px;
    font-weight: 600;
    font-size: 22px;
    color: var(--ink);
  }
  .brand .dot { width: 14px; height: 14px; border-radius: 50%; background: var(--ink); }
  .title {
    position: absolute;
    left: 410px; top: 50px;
    width: 620px;
    font-family: "Pinyon Script", cursive;
    font-weight: 400;
    font-size: 62px;
    line-height: 1.2;
    color: var(--ink);
    white-space: nowrap;
  }
  .date-line {
    position: absolute;
    left: 430px; top: 170px;
    font-family: "Lora", Georgia, serif;
    font-size: 20px;
    color: var(--ink-soft);
    display: flex; align-items: baseline; gap: 8px;
  }
  .blank { display: inline-block; border-bottom: 1px solid var(--rule); height: 1px; }
  .name-rule {
    position: absolute;
    left: 430px; top: 285px;
    width: 560px; height: 1.5px;
    background: var(--rule);
  }
  .statement {
    position: absolute;
    left: 430px; top: 300px;
    width: 540px;
    font-size: 13.5px;
    line-height: 1.5;
    color: var(--ink);
    text-align: center;
  }
  .seal {
    position: absolute;
    left: 985px; top: 330px;
    width: 70px; height: 70px;
    border-radius: 50%;
    background: radial-gradient(circle at 40% 38%, var(--seal) 55%, var(--seal-dark) 100%);
  }
  .signature-mark {
    position: absolute;
    left: 560px; top: 440px;
    width: 180px; height: 48px;
    background: linear-gradient(90deg, rgba(47,39,36,.12), rgba(47,39,36,.04));
    border-radius: 4px;
  }
  .signature-rule {
    position: absolute;
    left: 560px; top: 494px;
    width: 230px; height: 1px;
    background: var(--rule);
  }
  .signatory {
    position: absolute;
    left: 560px; top: 500px;
    font-family: "Lora", Georgia, serif;
    font-style: italic;
    font-weight: 600;
    font-size: 22px;
  }
  .signatory-role {
    position: absolute;
    left: 610px; top: 534px;
    font-size: 14px;
    color: var(--ink);
  }
</style>
</head>
<body>
  <main class="certificate">
    <div class="watermark" aria-hidden="true"></div>

    <ul class="maxims">
      <li>This is Lumen Stretch</li>
      <li>Breath is primary</li>
      <li>Evolve the physical culture</li>
      <li>Bring your unique<br>expression to the practice</li>
      <li>Take Breaks</li>
      <li>Freestyle</li>
      <li>Close your eyes</li>
      <li>Feel deeper into your body</li>
      <li>This is active meditation</li>
      <li>This is moving meditation</li>
      <li>This is modern meditation</li>
    </ul>

    <div class="column-rule" aria-hidden="true"></div>

    <div class="brand"><span class="dot" aria-hidden="true"></span>Lumen Stretch</div>

    <h1 class="title">Certificate of Completion</h1>

    <p class="date-line">On this day <span class="blank" style="width:80px"></span> day of <span class="blank" style="width:140px"></span>, <span class="blank" style="width:70px"></span>.</p>

    <div class="name-rule" aria-hidden="true"></div>

    <p class="statement">has successfully completed the Lumen Stretch modern vinyasa yoga training, completing two hundred hours of instruction in practice and theory. Within the power of our institution as a certifying agent we declare Such-and-such, now, a teacher competent to share the gift of yoga with the masses in a safe and effective</p>

    <div class="seal" aria-hidden="true"></div>

    <div class="signature-mark" role="img" aria-label="Handwritten signature of Dennis Whitcombe"></div>
    <div class="signature-rule" aria-hidden="true"></div>
    <p class="signatory">Dennis Whitcombe</p>
    <p class="signatory-role">Lumen Stretch founder</p>
  </main>
</body>
</html>
```